Thornfield Marsh, LLC Website

We are a small law firm in need of a website that contains the following:
1. Attractive main page
2. About us/attorney info for three people: Leonard Thornfield (attorney), Brent Marsh (attorney), and Melinda Carrow (legal assistant). We have bio's ready to submit.
3. Blog/video page. We'd like to post blogs and videos to help drive traffic
4. Multidistrict Litigation and Class Actions page, where we post information regarding active MDLs and Class actions that we are doing intake on.
Updates

Can you also please use the color "gold" in the design and logo? Thanks.

Industry/Entity Type

Legal

Coding

Coded - Design and coding required

Number of Pages Required

1 page

Colors
0054AA
0677BA
7BADD7
CADEEF
E8F1F8

Requirements
Must have
• 1. Attractive main page 2. About us/attorney info for three people: Leonard Thornfield (attorney), Brent Marsh (attorney), and Melinda Carrow (legal assistant). We have bio's ready to submit. 3. Blog/video page. We'd like to post blogs and videos to help drive traffic 4. Multidistrict Litigation and Class Actions page, where we post information regarding active MDLs and Class actions that we are doing intake on.

```html
<!DOCTYPE html>
<html lang="en">
<head>
<meta charset="UTF-8">
<title>Thornfield Marsh, LLC — Lawyers</title>
<link href="https://fonts.googleapis.com/css2?family=Lexend:wght@300;400;500;600&display=swap" rel="stylesheet">
<style>
:root{
  --blue-deep:#0054AA;
  --blue:#0677BA;
  --blue-mid:#7BADD7;
  --blue-soft:#CADEEF;
  --blue-pale:#E8F1F8;
  --gold:#C9A24A;
  --ink:#111820;
  --muted:#4a5563;
  --white:#ffffff;
}
*{box-sizing:border-box;margin:0;padding:0}
html,body{width:1200px;height:4301px;overflow:hidden}
body{font-family:'Lexend',sans-serif;color:var(--ink);background:var(--white);position:relative}
.abs{position:absolute}
.photo{position:absolute;border-radius:4px}
.btn{position:absolute;display:flex;align-items:center;justify-content:center;border-radius:6px;font-size:13px;font-weight:500}
.btn-blue{background:var(--blue-deep);color:var(--white)}
.btn-white{background:var(--white);color:var(--ink);box-shadow:0 2px 6px rgba(0,0,0,.15)}

/* header */
.hero{position:absolute;left:0;top:0;width:1200px;height:728px;background:linear-gradient(180deg,#3d6fb4 0%,#5b8fcd 45%,#2f6fc0 100%)}
.logo{position:absolute;display:flex;align-items:center;gap:10px;background:var(--white);border:2px solid var(--blue-deep);padding:6px 12px}
.logo-mark{width:26px;height:26px;background:var(--blue-deep)}
.logo-name{font-size:18px;font-weight:600;color:var(--blue-deep);letter-spacing:.3px}
.topline{font-size:12px;color:var(--ink)}
.nav a{position:absolute;top:90px;font-size:14px;font-weight:500;color:var(--ink);text-decoration:none}
.social{position:absolute;width:12px;height:12px;border-radius:50%;background:var(--ink)}
.hero-title{left:60px;top:238px;font-size:46px;font-weight:500;color:var(--white);line-height:1.1}
.hero-sub{left:60px;top:296px;font-size:25px;font-weight:400;color:var(--white)}
.hero-text{left:60px;top:346px;width:420px;font-size:14px;line-height:24px;color:var(--white);font-weight:300}

/* about */
.eyebrow{font-size:21px;font-weight:400}
.h2{font-size:34px;font-weight:500;line-height:1.2}
.tabs{position:absolute;left:599px;top:1048px;width:456px;height:40px;background:var(--blue-pale);border-radius:20px;display:flex;align-items:center;padding:0 8px;font-size:17px}
.tabs span{padding:0 12px}
.tabs .active{color:var(--blue-deep)}
.tabs .sep{width:1px;height:20px;background:var(--ink);padding:0}
.body-text{font-size:14px;line-height:24px;color:var(--muted);font-weight:300}

/* stats */
.stat{position:absolute;width:260px;text-align:center}
.stat b{display:block;font-size:52px;font-weight:500;color:var(--blue-deep);line-height:1}
.stat span{display:block;font-size:22px;font-weight:300;margin-top:8px}

/* blog */
.blog{position:absolute;left:0;top:1669px;width:1200px;height:676px;background:linear-gradient(180deg,#e8eef6 0%,#9bbde0 40%,#2f68b4 100%)}
.card{position:absolute;width:347px;background:var(--white);border-radius:6px;box-shadow:0 4px 14px rgba(0,0,0,.12);text-align:center;padding-bottom:16px}
.card .pic{width:327px;height:240px;margin:10px auto 0;border-radius:4px}
.card h3{font-size:18px;font-weight:500;margin-top:14px}
.card p{font-size:13px;font-weight:300;color:var(--muted);line-height:20px;margin:6px 20px 0}
.card .more{font-size:12px;font-weight:600;margin-top:10px}

/* practice */
.practice{position:absolute;width:255px;text-align:center}
.practice .pic{width:255px}
.practice h3{font-size:18px;font-weight:500;margin-top:22px}
.practice p{font-size:13px;font-weight:300;color:var(--muted);line-height:20px;margin-top:4px}
.practice .more{font-size:13px;font-weight:500;margin-top:10px}

/* contact */
.contact{position:absolute;left:60px;top:3251px;width:1080px;height:615px;border:2px solid #eceff3;border-radius:8px}
.label{position:absolute;left:492px;font-size:17px;font-weight:500}
.field{position:absolute;left:487px;width:601px;height:50px;background:#f1f3f6;border:1px solid #b9bfc8;border-radius:4px}

/* footer */
.footer{position:absolute;left:0;top:3956px;width:1200px;height:345px;background:linear-gradient(180deg,#2a5db0,#0054AA)}
.fcol{position:absolute;top:4020px;color:var(--white);font-size:14px}
.fcol h4{font-size:14px;font-weight:500;margin-bottom:22px}
.fcol p{font-weight:300;line-height:34px}
.fsocial{position:absolute;top:4196px;width:26px;height:26px;border-radius:50%;background:var(--white)}
</style>
</head>
<body>

<!-- Hero -->
<section class="hero">
  <div class="photo" role="img" aria-label="Courthouse columns and sculpture backdrop" style="left:0;top:0;width:1200px;height:728px;background:linear-gradient(180deg,rgba(220,230,245,.55),rgba(60,110,185,.2));border-radius:0"></div>
  <div class="photo" role="img" aria-label="Three attorneys standing together holding tablets" style="left:450px;top:218px;width:750px;height:510px;background:linear-gradient(180deg,#2a3550 0%,#1d2233 60%,#303a55 100%);border-radius:180px 180px 0 0;opacity:.85"></div>
  <div class="photo" role="img" aria-label="Judge's gavel, scales of justice and law books" style="left:0;top:575px;width:500px;height:225px;background:linear-gradient(135deg,#7a4a22,#c9a24a 50%,#e9e3d6);border-radius:60px 20px 40px 10px"></div>
</section>

<div class="logo" style="left:60px;top:12px">
  <div class="logo-mark"></div>
  <div class="logo-name">THORNFIELD MARSH LLC</div>
</div>
<svg class="abs" style="left:612px;top:27px" width="12" height="12" viewBox="0 0 24 24"><path d="M6.6 10.8a15 15 0 006.6 6.6l2.2-2.2a1 1 0 011-.25 11.4 11.4 0 003.6.57 1 1 0 011 1V20a1 1 0 01-1 1A17 17 0 013 4a1 1 0 011-1h3.5a1 1 0 011 1c0 1.25.2 2.45.57 3.57a1 1 0 01-.25 1z" fill="#111820"/></svg>
<div class="abs topline" style="left:630px;top:27px">(215) 555-0148</div>
<div class="abs topline" style="left:736px;top:27px">Monday - Friday: 8:00 AM - 9:00 PM</div>
<div class="btn btn-blue" style="left:955px;top:12px;width:185px;height:43px">Book A Consultation</div>
<div class="abs" style="left:60px;top:75px;width:1080px;height:1px;background:rgba(17,24,32,.4)"></div>
<div class="social" style="left:60px;top:92px"></div>
<div class="social" style="left:85px;top:92px"></div>
<div class="social" style="left:110px;top:92px"></div>
<div class="social" style="left:135px;top:92px"></div>
<nav class="nav">
  <a style="left:739px">Home</a>
  <a style="left:825px">About Us</a>
  <a style="left:930px">Blog</a>
  <a style="left:1005px">MDL &amp; Class Actions</a>
</nav>
<div class="abs hero-title">PROTECTING YOUR</div>
<div class="abs hero-sub">RIGHTS WITH PRECISION AND CARE</div>
<div class="abs hero-text">Lorem Ipsum Dolor Sit Amet Consectetur. Mauris Enim Dapibus Mauris Leo Senectus Lorem Ipsum Dolor Sit Amet Consectetur.</div>
<div class="btn btn-white" style="left:60px;top:450px;width:125px;height:46px">Learn More</div>

<!-- About -->
<div class="photo" role="img" aria-label="Classical courthouse statue and columns" style="left:108px;top:876px;width:282px;height:347px;background:linear-gradient(135deg,#d8dde3,#7f8894 60%,#3f6bb0)"></div>
<div class="photo" role="img" aria-label="Attorney signing documents at a desk" style="left:255px;top:1038px;width:284px;height:347px;background:linear-gradient(160deg,#5a6e88,#2b3140 55%,#7a5a3a)"></div>
<div class="abs eyebrow" style="left:599px;top:905px">About Us</div>
<div class="abs h2" style="left:599px;top:945px;width:520px">Expert Lawyers With A Passion For Justice</div>
<div class="tabs"><span class="active">Leonard Thornfield</span><span class="sep"></span><span>Brent Marsh</span><span class="sep"></span><span>Melinda Carrow</span></div>
<div class="abs body-text" style="left:599px;top:1125px;width:440px">Lorem Ipsum Dolor Sit Consectetur. Mauris Enim Dapibus Mauris Leo Senectus Lorem Ipsum Lorem Ipsum Dolor Sit Consectetur. Mauris Lorem Ipsum Dolor Sit Consectetur. Mauris Enim Dapibus Mauris Leo Senectus Lorem Ipsum Lorem Ipsum Dolor Sit Consectetur. Mauris Lorem Ipsum Dolor Sit Consectetur. Mauris Enim Dapibus Mauris Leo Senectus Lorem Ipsum Lorem Ipsum Dolor Sit Consectetur. Mauris</div>
<div class="btn btn-blue" style="left:599px;top:1317px;width:125px;height:43px">Learn More</div>

<!-- Stats -->
<div class="stat" style="left:60px;top:1494px"><b>2000+</b><span>Happy Client</span></div>
<div class="stat" style="left:342px;top:1494px"><b>150+</b><span>Attorneys</span></div>
<div class="stat" style="left:616px;top:1494px"><b>1500+</b><span>Practice Area</span></div>
<div class="stat" style="left:895px;top:1494px"><b>50+</b><span>Case Dismis</span></div>

<!-- Blog -->
<section class="blog"></section>
<div class="abs eyebrow" style="left:0;top:1715px;width:1200px;text-align:center">Blog</div>
<div class="abs h2" style="left:0;top:1755px;width:1200px;text-align:center">Breaking Down Complex Legal Topics, One Post At A Time</div>
<article class="card" style="left:60px;top:1920px">
  <div class="pic" role="img" aria-label="Hand signing paperwork beside scales" style="background:linear-gradient(135deg,#2a2620,#6b5a3c 55%,#e8e6e0)"></div>
  <h3>Legal Insights To Empower</h3>
  <p>Lorem Ipsum Dolor Sit Amet Consectetur. Quis Suspendisse A Egestas Consequat.</p>
  <div class="more">Read More &nbsp;»</div>
</article>
<article class="card" style="left:427px;top:1853px">
  <div class="pic" role="img" aria-label="Gavel and scales on a desk with a lawyer writing" style="background:linear-gradient(135deg,#3a2a1c,#8a6a44 50%,#d9d4cc)"></div>
  <h3>Legal Insights To Empower</h3>
  <p>Lorem Ipsum Dolor Sit Amet Consectetur. Quis Suspendisse A Egestas Consequat.</p>
  <div class="more">Read More &nbsp;»</div>
</article>
<article class="card" style="left:793px;top:1920px">
  <div class="pic" role="img" aria-label="Stack of business law books with a gavel" style="background:linear-gradient(135deg,#3a2416,#8a5a2c 50%,#c9a24a)"></div>
  <h3>Legal Insights To Empower</h3>
  <p>Lorem Ipsum Dolor Sit Amet Consectetur. Quis Suspendisse A Egestas Consequat.</p>
  <div class="more">Read More &nbsp;»</div>
</article>
<div class="btn btn-white" style="left:527px;top:2258px;width:146px;height:45px">Discover More</div>

<!-- MDL -->
<div class="abs eyebrow" style="left:60px;top:2470px">MDL &amp; Class Actions</div>
<div class="abs h2" style="left:60px;top:2510px">Fighting For Justice—Together</div>
<div class="abs body-text" style="left:756px;top:2435px;width:390px">Lorem Ipsum Dolor Sit Consectetur. Mauris Enim Dapibus Mauris Leo Senectus Lorem Ipsum Lorem Ipsum Dolor Sit Consectetur. Mauris</div>
<div class="btn btn-blue" style="left:756px;top:2534px;width:145px;height:43px">Discover More</div>

<div class="practice" style="left:60px;top:2637px">
  <div class="pic photo" role="img" aria-label="Family meeting with an attorney" style="position:relative;height:267px;background:linear-gradient(135deg,#6c7a8c,#2d3544 60%,#a9b3bf)"></div>
  <h3>Family Law</h3><p>Lorem Ipsum Dolor Sit Amet<br>Consectetur. Quis</p><div class="more">Learn More</div>
</div>
<div class="practice" style="left:335px;top:2637px">
  <div class="pic photo" role="img" aria-label="Injured client consulting a lawyer" style="position:relative;height:412px;background:linear-gradient(160deg,#d9d2c6,#8a94a2 50%,#4a3a30)"></div>
  <h3 style="margin-top:20px">Personal Injury Law</h3><p>Lorem Ipsum Dolor Sit Amet<br>Consectetur. Quis</p><div class="more">Learn More</div>
</div>
<div class="practice" style="left:611px;top:2637px">
  <div class="pic photo" role="img" aria-label="Lawyer signing a business contract" style="position:relative;height:412px;background:linear-gradient(160deg,#1e2430,#3a4150 55%,#d8dadd)"></div>
  <h3 style="margin-top:20px">Business Law</h3><p>Lorem Ipsum Dolor Sit Amet<br>Consectetur. Quis</p><div class="more">Learn More</div>
</div>
<div class="practice" style="left:885px;top:2637px">
  <div class="pic photo" role="img" aria-label="Handcuffed hands over legal documents" style="position:relative;height:267px;background:linear-gradient(135deg,#5a4a40,#2a2a2e 55%,#9a8a78)"></div>
  <h3>Criminal Defense Law</h3><p>Lorem Ipsum Dolor Sit Amet<br>Consectetur. Quis</p><div class="more">Learn More</div>
</div>

<!-- Contact -->
<section class="contact"></section>
<div class="photo" role="img" aria-label="Wooden gavel on its sound block" style="left:60px;top:3251px;width:374px;height:615px;background:linear-gradient(160deg,#2f4f86,#6a3a1c 55%,#c9a24a);border-radius:8px 0 0 8px"></div>
<div class="abs h2" style="left:486px;top:3300px">Contact Us</div>
<div class="label" style="top:3364px">Name</div><div class="field" style="top:3400px"></div>
<div class="label" style="top:3465px">Email</div><div class="field" style="top:3501px"></div>
<div class="label" style="top:3567px">Addess</div><div class="field" style="top:3605px;left:485px;width:603px"></div>
<div class="label" style="top:3664px">Phone Number</div><div class="field" style="top:3700px;left:485px;width:603px"></div>
<div class="btn btn-blue" style="left:485px;top:3780px;width:603px;height:44px;font-size:16px">Submit</div>

<!-- Footer -->
<footer class="footer"></footer>
<div class="logo" style="left:60px;top:4019px">
  <div class="logo-mark"></div>
  <div class="logo-name">THORNFIELD MARSH LLC</div>
</div>
<div class="abs" style="left:60px;top:4105px;width:370px;font-size:14px;line-height:24px;color:var(--white);font-weight:300">Lorem Ipsum Dolor Consectetur. Platea Cursus Amet Elementum Varius Vitae Lorem Ipsum Dolor Consectetur.</div>
<div class="fsocial" style="left:60px"></div>
<div class="fsocial" style="left:101px"></div>
<div class="fsocial" style="left:142px"></div>
<div class="fsocial" style="left:183px"></div>
<div class="fcol" style="left:551px"><h4 style="text-decoration:underline">Home</h4><p style="margin-top:20px">Lorem Ipsum<br>Dolor Sit<br>Amet</p></div>
<div class="fcol" style="left:704px"><h4>About Us</h4><p>Lorem<br>Ipsum Dolor<br>Sit Amet<br>Consectetur.</p></div>
<div class="fcol" style="left:851px"><h4>Blog</h4><p>Lorem Ipsum<br>Dolor Sit<br>Amet<br>Consectetur.</p></div>
<div class="fcol" style="left:1005px"><h4>MDL &amp; Class Actions</h4><p>Lorem Ipsum<br>Dolor Sit Amet</p></div>
<div class="abs" style="left:60px;top:4248px;width:1080px;height:1px;background:rgba(255,255,255,.6)"></div>
<div class="abs" style="left:60px;top:4269px;font-size:11px;color:var(--white);font-weight:300">Copyright © 2025 All Right Reserved</div>
<div class="abs" style="left:798px;top:4269px;font-size:11px;color:var(--white);font-weight:300">Privacy Policy</div>
<div class="abs" style="left:905px;top:4269px;font-size:11px;color:var(--white);font-weight:300">Terms Of Service</div>
<div class="abs" style="left:1029px;top:4269px;font-size:11px;color:var(--white);font-weight:300">Cookies Settings</div>

</body>
</html>
```